Business Card for Bramble Gear

Target Market(s)

Mining, fleet, 4wd industry

Industry/Entity Type

Business

Requirements
Must have
• Front of card
Logo of Bramble Gear, the Nut preferrably top right corner and wording which says
"The Classic Kordo Bolt Products along bottom right hand corner
Use of the orange logo.
Back of card down left side to include (bullet points )
. Canvas Seat Covers
. Hi - Vis Flags
. Canvas or PVC designs by request.
back of card down right side
Danielle Rowbeck
Ph 02 49315728
E ; admin@bramblegear.com.au
W: www.bramblegear.com.au
Nice to have
• other designs can also be submitted as we require additional cards.

```html
<!DOCTYPE html>
<html lang="en">
<head>
<meta charset="utf-8">
<title>Bramble Gear — Business Card</title>
<link href="https://fonts.googleapis.com/css2?family=Open+Sans:wght@400;800&display=swap" rel="stylesheet">
<style>
  :root {
    --brand-orange: #f7941d;
    --brand-grey: #7f7f7f;
    --text-light: #ffffff;
    --backdrop: #d9d9d9;
    --nut-brown: #8a4a2c;
    --nut-tan: #c98a5a;
    --card-w: 640px;
    --card-h: 366px;
  }
  * { box-sizing: border-box; margin: 0; padding: 0; }
  html, body {
    width: 1200px;
    height: 900px;
    overflow: hidden;
  }
  body {
    background: var(--backdrop);
    font-family: "Open Sans", Arial, sans-serif;
    display: flex;
    flex-direction: column;
    align-items: center;
    justify-content: center;
    gap: 40px;
  }
  .card {
    position: relative;
    width: var(--card-w);
    height: var(--card-h);
    background: var(--brand-orange);
    overflow: hidden;
    box-shadow: 0 6px 18px rgba(0,0,0,0.18);
  }
  .card-shapes {
    position: absolute;
    inset: 0;
    width: 100%;
    height: 100%;
  }
  .shape-grey { fill: var(--brand-grey); }
  .shape-orange { fill: var(--brand-orange); }

  /* Front */
  .brand-name {
    position: absolute;
    left: 40px;
    top: 150px;
    font-weight: 800;
    font-size: 46px;
    letter-spacing: -1px;
    text-transform: uppercase;
    color: var(--text-light);
    line-height: 1;
  }
  .mascot {
    position: absolute;
    right: 44px;
    top: 26px;
    width: 120px;
    height: 110px;
    border-radius: 50%;
    background: radial-gradient(circle at 40% 40%, var(--nut-tan), var(--nut-brown));
  }
  .tagline {
    position: absolute;
    right: 30px;
    bottom: 26px;
    font-weight: 400;
    font-size: 19px;
    color: var(--text-light);
  }

  /* Back */
  .services {
    position: absolute;
    left: 40px;
    bottom: 40px;
    list-style: none;
    color: var(--text-light);
    font-size: 17px;
    line-height: 1.55;
  }
  .services li::before {
    content: "";
    display: inline-block;
    width: 8px;
    height: 8px;
    border-radius: 50%;
    background: var(--brand-orange);
    margin-right: 12px;
    vertical-align: middle;
  }
  .contact {
    position: absolute;
    right: 40px;
    top: 70px;
    color: var(--text-light);
    font-size: 16px;
    line-height: 1.5;
    font-style: normal;
  }
</style>
</head>
<body>

  <section class="card card-front" aria-label="Front of card">
    <svg class="card-shapes" viewBox="0 0 640 366" preserveAspectRatio="none" aria-hidden="true">
      <polygon class="shape-grey" points="0,230 0,366 430,366"/>
    </svg>
    <div class="brand-name">Bramble Gear</div>
    <div class="mascot" role="img" aria-label="Kordo Bolt mascot illustration: cartoon walnut character with gloved hands"></div>
    <p class="tagline">The Classic Kordo Bolt Products</p>
  </section>

  <section class="card card-back" aria-label="Back of card">
    <svg class="card-shapes" viewBox="0 0 640 366" preserveAspectRatio="none" aria-hidden="true">
      <rect class="shape-grey" width="640" height="366"/>
      <polygon class="shape-orange" points="50,0 640,0 640,130 0,250 0,60"/>
    </svg>
    <address class="contact">
      Danielle Rowbeck<br>
      Ph: 02 49315728<br>
      E : admin@bramblegear.com.au<br>
      W: www.bramblegear.com.au
    </address>
    <ul class="services">
      <li>Hi - Vis Flags</li>
      <li>Canvas Seat Covers</li>
      <li>Canvas or PVC designs by request</li>
    </ul>
  </section>

</body>
</html>
```